Business Card Thorne Landscaping
Professional
Peter Thorne
P.O. Box 7634
Alder St.
Birchmont Vermont 04318
peter@thornelandscaping.example
www.thornelandscaping.example
As a possibility it might be nice to incorporated the service we offer on the card they are Design / Build, Landscape Management, Turf and Snow. If this doesn't make the card not a big deal.
I would like to the see the option on the back of the card being green with just our logo in white or even just the symbol part of our logo.

```html
<!DOCTYPE html>
<html lang="en">
<head>
<meta charset="utf-8">
<title>Thorne Landscaping – Business Cards</title>
<link href="https://fonts.googleapis.com/css2?family=Libre+Baskerville:wght@700&family=Arimo:wght@400;700&display=swap" rel="stylesheet">
<style>
  :root {
    --green: #1f6b3a;
    --green-dark: #175a2f;
    --white: #ffffff;
    --card-white: #f7f7f7;
    --swoosh: #b9b9b9;
    --backdrop: #ebe8e3;
  }
  * { box-sizing: border-box; margin: 0; padding: 0; }
  html, body { width: 1200px; height: 763px; overflow: hidden; }
  body {
    background: var(--backdrop);
    position: relative;
    font-family: "Arimo", Arial, sans-serif;
  }
  .card {
    position: absolute;
    border-radius: 14px;
    overflow: hidden;
    box-shadow: 0 4px 12px rgba(0,0,0,0.12);
  }

  /* Front card */
  .card-front { left: 113px; top: 119px; width: 499px; height: 282px; background: var(--card-white); }
  .card-front .band { position: absolute; inset: 0; }
  .brand-front {
    position: absolute; left: 0; right: 0; top: 34px;
    display: flex; align-items: center; justify-content: center; gap: 14px;
  }
  .brand-mark { width: 46px; height: 46px; border-radius: 50%; background: var(--green); flex: none; }
  .brand-name {
    font-family: "Libre Baskerville", Georgia, serif; font-weight: 700;
    color: var(--green); font-size: 32px; line-height: 1; white-space: nowrap;
  }
  .tagline {
    position: absolute; left: 0; right: 0; top: 98px; text-align: center;
    font-size: 8.5px; letter-spacing: 2px; color: var(--green); font-weight: 700;
  }
  .contact-block {
    position: absolute; top: 180px; left: 0; right: 0; height: 84px;
    color: var(--white); font-size: 10.5px; line-height: 1.45;
  }
  .person { position: absolute; right: 258px; text-align: right; }
  .person-name { font-size: 14px; font-weight: 700; }
  .person-title { font-size: 10px; margin-bottom: 10px; }
  .divider { position: absolute; left: 252px; top: 2px; width: 1px; height: 76px; background: var(--white); }
  .details { position: absolute; left: 266px; }
  .details .web { margin-top: 10px; }

  /* Green back */
  .card-back-green {
    left: 653px; top: 60px; width: 432px; height: 281px; background: var(--green);
    display: flex; flex-direction: column; align-items: center; justify-content: center; gap: 24px;
  }
  .card-back-green .brand-mark { background: var(--white); }
  .card-back-green .brand-name { color: var(--white); }
  .card-back-green .web-back { color: var(--white); }

  /* White back */
  .card-back-white {
    left: 353px; top: 382px; width: 494px; height: 281px; background: var(--card-white);
    display: flex; flex-direction: column; align-items: center; justify-content: center; gap: 24px;
  }
  .brand-back { display: flex; align-items: center; gap: 12px; }
  .brand-back .brand-mark { width: 40px; height: 40px; }
  .brand-back .brand-name { font-size: 24px; }
  .web-back { font-size: 16px; font-weight: 700; color: var(--green); }
</style>
</head>
<body>

<section class="card card-front" aria-label="Business card front">
  <svg class="band" viewBox="0 0 499 282" width="499" height="282" aria-hidden="true">
    <path d="M0 146 C 140 112, 300 172, 499 122" fill="none" stroke="var(--swoosh)" stroke-width="5"/>
    <path d="M0 164 C 150 130, 320 182, 499 138 L499 282 L0 282 Z" fill="var(--green)"/>
    <path d="M0 164 C 150 130, 320 182, 499 138" fill="none" stroke="var(--green-dark)" stroke-width="3"/>
  </svg>
  <div class="brand-front">
    <span class="brand-mark"></span>
    <span class="brand-name">Thorne Landscaping</span>
  </div>
  <p class="tagline">FOR THOSE WHO EXPECT THE BEST</p>
  <div class="contact-block">
    <div class="person">
      <p class="person-name">Peter Thorne</p>
      <p class="person-title">President</p>
      <p>P.O. Box 7634, Alder St.</p>
      <p>Birchmont Vermont 04318</p>
    </div>
    <span class="divider"></span>
    <div class="details">
      <p>Phone: 207-555-0148</p>
      <p>Fax: 207-555-0193</p>
      <p>Email: peter@thornelandscaping.example</p>
      <p class="web">www.thornelandscaping.example</p>
    </div>
  </div>
</section>

<section class="card card-back-green" aria-label="Business card back, green">
  <div class="brand-back">
    <span class="brand-mark"></span>
    <span class="brand-name">Thorne Landscaping</span>
  </div>
  <p class="web-back">www.thornelandscaping.example</p>
</section>

<section class="card card-back-white" aria-label="Business card back, white">
  <div class="brand-back">
    <span class="brand-mark"></span>
    <span class="brand-name">Thorne Landscaping</span>
  </div>
  <p class="web-back">www.thornelandscaping.example</p>
</section>

</body>
</html>
```